Training Company Needs a Web Design

We are a Training company that needs a website design completed for us. "The Harbor Loft" The website will be a 'community space' specialising in 'Change and Transformation'. It will be a 'space' where individuals can come to find out 'latest news', upcoming events and courses, chat with others and find 'tools and templates'. They will need to login as a 'Member'.

The final design needs to be professional but have a 'fun and interactive' feel and appeal to our target audience who are predominantly corporate individuals.

Target Market(s)

Corporate Individuals - they may have a Change or Project background

Industry/Entity Type

Business Consultant

Number of Pages Required

3 page

Font styles to use
Sans Serif

Requirements
Must have
• Design for 'Home Page'
• A professional and corporate 'feel' but be fun and interactive.
Nice to have
• A 'sense' of how some of the other pages may be designed or laid out.

```html
<!DOCTYPE html>
<html lang="en">
<head>
<meta charset="utf-8">
<title>The Harbor Loft – Home</title>
<link href="https://fonts.googleapis.com/css2?family=Open+Sans:wght@400;600;700&family=Roboto+Condensed:wght@300;400;700&display=swap" rel="stylesheet">
<style>
:root{
  --orange:#e8452b;
  --blue:#0d4d92;
  --navy:#0b3f7a;
  --purple:#7c63a9;
  --purple-dark:#5f4a8a;
  --yellow:#f2c414;
  --yellow-dark:#d79b0c;
  --teal:#3fd1b2;
  --teal-dark:#22a98c;
  --mint:#3dd8b2;
  --ink:#222;
  --text:#555;
  --muted:#888;
  --grey:#e9e9e9;
  --grey-band:#dcdcdc;
}
*{box-sizing:border-box;margin:0;padding:0}
html,body{width:1200px;height:4317px;overflow:hidden}
body{position:relative;background:#fff;font-family:"Open Sans",Arial,sans-serif;color:var(--text)}
.abs{position:absolute}
h2,.eyebrow,.hero-title{font-family:"Roboto Condensed","Arial Narrow",sans-serif}
.eyebrow{color:var(--orange);font-size:15px;text-transform:uppercase;letter-spacing:.5px}
h2{color:var(--ink);font-size:29px;font-weight:700;text-transform:uppercase;letter-spacing:.5px;margin-top:4px}
.rule{width:72px;height:3px;background:var(--ink);margin-top:12px}
.btn{display:inline-block;background:var(--orange);color:#fff;font-size:12px;font-weight:700;text-transform:uppercase;padding:9px 16px;letter-spacing:.5px}

/* header */
.site-header{left:0;top:0;width:1200px;height:104px;background:#fff;box-shadow:0 2px 6px rgba(0,0,0,.08);z-index:3}
.brand{left:86px;top:26px;display:flex;align-items:center;gap:12px}
.brand-square{width:46px;height:46px;border:5px solid var(--blue)}
.brand-name{color:var(--blue);font-weight:700;font-size:18px;line-height:20px;width:120px;text-transform:uppercase}
.main-nav{left:312px;top:40px;display:flex;gap:34px;font-size:15px;text-transform:uppercase;color:#666}
.main-nav .active{color:var(--blue);font-weight:700}
.member-login{left:982px;top:26px;width:130px;height:62px;background:var(--mint);border-radius:4px;display:flex;align-items:center;gap:10px;padding-left:16px;color:var(--navy);font-weight:700;font-size:14px;line-height:15px}
.member-login span.ico{width:26px;height:26px;border-radius:50%;background:var(--navy)}

/* hero */
.hero{left:0;top:104px;width:1200px;height:633px;background:linear-gradient(160deg,#c9b07a 0%,#8b8f8e 35%,#4e6584 65%,#2f3f5e 100%)}
.hero-shade{inset:0;background:rgba(20,25,40,.25)}
.hero-frame{left:331px;top:256px;width:532px;height:244px;border:3px solid rgba(255,255,255,.75)}
.hero-title{left:0;top:268px;width:1200px;text-align:center;color:#fff;font-size:62px;font-weight:400;letter-spacing:1px}
.hero-sub{left:0;top:352px;width:1200px;text-align:center;color:#fff;font-size:16px;line-height:22px}
.hero-cta{left:532px;top:414px;width:136px;height:36px;background:var(--yellow);color:#222;font-size:13px;font-weight:700;text-align:center;line-height:36px;text-transform:uppercase}
.hero-arrow{top:296px;width:22px;height:40px}

/* about */
.about-back{left:115px;top:820px;width:345px;height:360px;background:#d3d3d3}
.about-frame{left:140px;top:840px;width:335px;height:338px;border:3px solid #fff;outline:1px solid #ccc}
.about-photo{left:187px;top:892px;width:331px;height:331px;background:linear-gradient(135deg,#8c6c4c,#c9a77a 45%,#5d5b6e)}
.about-text{left:639px;top:828px;width:512px}
.about-text p{margin-top:22px;font-size:14px;line-height:22px}
.about-text .btn{margin-top:34px}

/* services */
.band{left:0;width:1200px}
.section-head{left:0;width:1200px;padding-left:640px}
.service{width:260px;height:400px}
.service svg{position:absolute;inset:0}
.service-body{position:absolute;left:26px;top:90px;width:200px;color:#fff}
.service-body h3{font-family:"Roboto Condensed",sans-serif;font-size:23px;font-weight:400;text-transform:uppercase;letter-spacing:.5px}
.service-body p{font-size:13px;line-height:19px;margin-top:12px}
.service-icon{position:absolute;left:26px;top:36px}

/* events */
.view-more{width:110px;height:32px;background:var(--orange);color:#fff;font-size:11px;font-weight:700;text-align:center;line-height:32px;text-transform:uppercase}
.event{width:246px;height:266px;border:10px solid var(--purple);background:#fff;padding:36px 16px 0}
.event-date{position:absolute;top:-28px;right:46px;width:80px;height:56px;background:#fff;text-align:center;font-family:"Roboto Condensed",sans-serif;font-weight:700;font-size:24px;line-height:24px;color:#222;padding-top:4px}
.event h4{font-size:13px;color:#222;line-height:18px;font-weight:700}
.event .place{font-size:12px;color:var(--muted);margin-top:8px}
.event p{font-size:12px;line-height:17px;margin-top:10px}
.circle-arrow{width:24px;height:24px;margin-top:14px}

/* speakers */
.speaker-card{left:161px;top:2685px;width:492px;height:466px;background:var(--blue);color:#fff;text-align:center;padding:0 32px}
.speaker-card .mic{width:66px;height:66px;border-radius:50%;background:var(--teal);margin:40px auto 0;display:flex;align-items:center;justify-content:center}
.speaker-card h4{font-size:15px;font-weight:700;text-transform:uppercase;margin-top:34px}
.speaker-card p{font-size:13px;line-height:20px;margin-top:24px}
.speaker-card .btn{margin-top:34px}
.speaker-photo{left:596px;top:2648px;width:434px;height:532px;background:#fff;padding:12px;box-shadow:0 4px 12px rgba(0,0,0,.18)}
.speaker-photo div{width:100%;height:100%;background:linear-gradient(160deg,#c9d6e6 0%,#9aaec6 40%,#3e4a5e 75%,#1e2533 100%)}

/* courses */
.course{width:245px;height:357px;background:#fff;border:1px solid #e2e2e2}
.course .ph{height:166px}
.course h4{font-size:14px;color:#222;font-weight:600;margin:20px 16px 0}
.course p{font-size:12px;line-height:17px;margin:10px 16px 0}
.course .circle-arrow{margin-left:16px}

/* footer */
.footer{left:0;top:3857px;width:1200px;height:359px;background:var(--grey)}
.contact-col{top:3917px;width:420px}
.contact-head{display:flex;align-items:center;gap:18px}
.contact-head .ic{width:62px;height:62px;border-radius:50%;background:var(--navy);display:flex;align-items:center;justify-content:center}
.contact-head h3{font-size:30px;font-weight:400;line-height:32px;color:var(--navy)}
.contact-head h3 span{color:#1f67b4}
.contact-col p{font-size:13px;line-height:19px;margin-top:24px}
.contact-col .small{margin-top:18px}
.sub-form{display:flex;gap:6px;margin-top:22px}
.sub-form .field{width:210px;height:32px;background:#fff;border-radius:16px;font-size:12px;color:#aaa;line-height:32px;padding-left:14px}
.sub-form .send{width:116px;height:32px;background:var(--orange);border-radius:16px;color:#fff;font-size:11px;font-weight:700;text-align:center;line-height:32px;text-transform:uppercase}

.bottom-bar{left:0;top:4216px;width:1200px;height:101px;background:#fff}
.socials{left:358px;top:4252px;display:flex;gap:6px}
.socials span{width:32px;height:32px;border-radius:50%;border:2px solid #999}
.copyright{left:764px;top:4250px;font-size:12px;line-height:18px;color:#444}
</style>
</head>
<body>

<header class="site-header abs">
  <div class="brand abs"><span class="brand-square"></span><span class="brand-name">The Harbor Loft</span></div>
  <nav class="main-nav abs"><span class="active">Home</span><span>About</span><span>Services</span><span>Courses</span><span>News</span><span>Events</span><span>Contact</span></nav>
  <div class="member-login abs"><span class="ico"></span><span>MEMBER<br>LOGIN</span></div>
</header>

<section class="hero abs" role="img" aria-label="Photo of a smiling group of corporate professionals gathered together">
  <div class="hero-shade abs"></div>
  <div class="hero-frame abs"></div>
  <h1 class="hero-title abs">THE HARBOR LOFT</h1>
  <p class="hero-sub abs">A 'community' where by an individual can go to learn,<br>connect, collaborate and share.</p>
  <div class="hero-cta abs">Get Started</div>
  <svg class="hero-arrow abs" style="left:14px" viewBox="0 0 22 40"><polyline points="18,4 4,20 18,36" fill="none" stroke="#fff" stroke-width="3"/></svg>
  <svg class="hero-arrow abs" style="left:1164px" viewBox="0 0 22 40"><polyline points="4,4 18,20 4,36" fill="none" stroke="#fff" stroke-width="3"/></svg>
</section>

<section class="about">
  <div class="about-back abs"></div>
  <div class="about-frame abs"></div>
  <div class="about-photo abs" role="img" aria-label="Photo of a group seated in a circle during a workshop"></div>
  <div class="about-text abs">
    <div class="eyebrow">Introduction</div>
    <h2>About The Harbor Loft</h2>
    <div class="rule"></div>
    <p>Lorem ipsum dolor sit amet, consectetur adipiscing elit, sed do eiusmod tempor incididunt ut labore et dolore magna aliqua. Ut enim ad minim veniam, quis nostrud exercitation ullamco laboris nisi ut aliquip ex ea commodo consequat. Duis aute irure dolor in reprehenderit in voluptate velit esse cillum dolore eu fugiat nulla pariatur. Excepteur sint occaecat cupidatat non proident, sunt in culpa qui officia deserunt mollit anim id est laborum. Excepteur sint occaecat cupidatat non proident.</p>
    <span class="btn">Read More &#8250;</span>
  </div>
</section>

<section class="services">
  <svg class="band abs" style="top:1200px" width="1200" height="800" viewBox="0 0 1200 800"><polygon points="0,130 1200,10 1200,700 0,790" fill="var(--grey-band)"/></svg>
  <div class="section-head abs" style="top:1350px;text-align:left"><div class="eyebrow">Lorem ipsum dolor</div><h2>Our Great Services</h2><div class="rule"></div></div>

  <div class="service abs" style="left:72px;top:1453px">
    <svg viewBox="0 0 260 400"><polygon points="210,30 258,40 258,380 210,360" fill="var(--purple-dark)"/><polygon points="0,0 240,28 240,400 0,372" fill="var(--purple)"/></svg>
    <svg class="service-icon" width="44" height="36" viewBox="0 0 44 36"><rect x="3" y="3" width="38" height="24" rx="2" fill="none" stroke="#fff" stroke-width="3"/><line x1="14" y1="33" x2="30" y2="33" stroke="#fff" stroke-width="3"/></svg>
    <div class="service-body"><h3>Learning</h3><p>Lorem ipsum dolor sit amet, consectetur adipiscing elit, sed do eiusmod tempor incididunt ut labore et dolore magna aliqua. Ut enim ad minim veniam, quis nostrud exercitation ullamco laboris nisi ut aliquip ex ea commodo consequat.</p></div>
  </div>

  <div class="service abs" style="left:342px;top:1455px">
    <svg viewBox="0 0 260 400"><polygon points="210,20 258,30 258,370 210,360" fill="var(--navy)"/><polygon points="0,20 240,0 240,372 0,400" fill="var(--blue)"/></svg>
    <svg class="service-icon" width="44" height="44" viewBox="0 0 44 44"><g stroke="#fff" stroke-width="3"><line x1="22" y1="22" x2="22" y2="5"/><line x1="22" y1="22" x2="6" y2="34"/><line x1="22" y1="22" x2="38" y2="34"/></g><g fill="#fff"><circle cx="22" cy="22" r="6"/><circle cx="22" cy="5" r="4"/><circle cx="6" cy="34" r="4"/><circle cx="38" cy="34" r="4"/></g></svg>
    <div class="service-body"><h3>Connecting</h3><p>Lorem ipsum dolor sit amet, consectetur adipiscing elit, sed do eiusmod tempor incididunt ut labore et dolore magna aliqua. Ut enim ad minim veniam, quis nostrud exercitation ullamco laboris nisi ut aliquip ex ea commodo consequat.</p></div>
  </div>

  <div class="service abs" style="left:613px;top:1476px">
    <svg viewBox="0 0 260 400"><polygon points="205,10 258,0 258,340 205,350" fill="var(--yellow-dark)"/><polygon points="0,30 240,10 240,380 0,400" fill="var(--yellow)"/></svg>
    <svg class="service-icon" style="top:56px" width="48" height="40" viewBox="0 0 48 40"><path d="M2 2h28v18H12l-6 6v-6H2z" fill="#fff"/><path d="M34 10h12v18h-4v6l-6-6H18v-4h16z" fill="#fff"/></svg>
    <div class="service-body" style="top:112px"><h3>Collaborating</h3><p>Lorem ipsum dolor sit amet, consectetur adipiscing elit, sed do eiusmod tempor incididunt ut labore et dolore magna aliqua. Ut enim ad minim veniam, quis nostrud exercitation ullamco laboris nisi ut aliquip ex ea commodo consequat.</p></div>
  </div>

  <div class="service abs" style="left:884px;top:1490px">
    <svg viewBox="0 0 260 400"><polygon points="210,40 258,50 258,400 210,380" fill="var(--teal-dark)"/><polygon points="0,0 240,30 240,400 0,380" fill="var(--teal)"/></svg>
    <svg class="service-icon" style="top:50px" width="40" height="44" viewBox="0 0 40 44"><g stroke="#fff" stroke-width="3"><line x1="10" y1="22" x2="30" y2="8"/><line x1="10" y1="22" x2="30" y2="36"/></g><g fill="#fff"><circle cx="10" cy="22" r="7"/><circle cx="30" cy="8" r="7"/><circle cx="30" cy="36" r="7"/></g></svg>
    <div class="service-body" style="top:108px"><h3>Sharing</h3><p>Lorem ipsum dolor sit amet, consectetur adipiscing elit, sed do eiusmod tempor incididunt ut labore et dolore magna aliqua. Ut enim ad minim veniam, quis nostrud exercitation ullamco laboris nisi ut aliquip ex ea commodo consequat.</p></div>
  </div>
</section>

<section class="events">
  <div class="abs" style="left:72px;top:1982px"><div class="eyebrow">Great Events</div><h2>Upcoming Events</h2><div class="rule"></div></div>
  <div class="view-more abs" style="left:1015px;top:2015px">View More &#8250;</div>

  <article class="event abs" style="left:72px;top:2124px"><div class="event-date">FEB<br>18</div><h4>Lorem ipsum dolor sit amet</h4><div class="place">London</div><p>Lorem ipsum dolor sit amet, consectetur adipiscing elit, sed diam nonummy nibh euismod tincidunt.</p><svg class="circle-arrow" viewBox="0 0 24 24"><circle cx="12" cy="12" r="10" fill="none" stroke="var(--purple)" stroke-width="2"/><path d="M7 12h9M12 8l4 4-4 4" fill="none" stroke="var(--purple)" stroke-width="2"/></svg></article>
  <article class="event abs" style="left:342px;top:2124px"><div class="event-date">FEB<br>18</div><h4>Lorem ipsum dolor sit amet</h4><div class="place">London</div><p>Lorem ipsum dolor sit amet, consectetur adipiscing elit, sed diam nonummy nibh euismod tincidunt.</p><svg class="circle-arrow" viewBox="0 0 24 24"><circle cx="12" cy="12" r="10" fill="none" stroke="var(--purple)" stroke-width="2"/><path d="M7 12h9M12 8l4 4-4 4" fill="none" stroke="var(--purple)" stroke-width="2"/></svg></article>
  <article class="event abs" style="left:613px;top:2124px"><div class="event-date">FEB<br>18</div><h4>Lorem ipsum dolor sit amet</h4><div class="place">London</div><p>Lorem ipsum dolor sit amet, consectetur adipiscing elit, sed diam nonummy nibh euismod tincidunt.</p><svg class="circle-arrow" viewBox="0 0 24 24"><circle cx="12" cy="12" r="10" fill="none" stroke="var(--purple)" stroke-width="2"/><path d="M7 12h9M12 8l4 4-4 4" fill="none" stroke="var(--purple)" stroke-width="2"/></svg></article>
  <article class="event abs" style="left:884px;top:2124px"><div class="event-date">FEB<br>18</div><h4>Lorem ipsum dolor sit amet</h4><div class="place">London</div><p>Lorem ipsum dolor sit amet, consectetur adipiscing elit, sed diam nonummy nibh euismod tincidunt.</p><svg class="circle-arrow" viewBox="0 0 24 24"><circle cx="12" cy="12" r="10" fill="none" stroke="var(--purple)" stroke-width="2"/><path d="M7 12h9M12 8l4 4-4 4" fill="none" stroke="var(--purple)" stroke-width="2"/></svg></article>
</section>

<section class="speakers">
  <svg class="band abs" style="top:2470px" width="1200" height="760" viewBox="0 0 1200 760"><polygon points="0,70 1200,10 1200,754 0,754" fill="var(--grey-band)"/></svg>
  <div class="abs" style="left:0;top:2540px;width:1200px;text-align:center"><div class="eyebrow">Lorem ipsum dolor</div><h2 style="font-size:28px">Speakers and Webinars</h2><div class="rule" style="margin:12px auto 0"></div></div>
  <svg class="abs" style="left:72px;top:2890px" width="50" height="100" viewBox="0 0 50 100"><polyline points="46,2 4,50 46,98" fill="none" stroke="#999" stroke-width="2"/></svg>
  <svg class="abs" style="left:1078px;top:2890px" width="50" height="100" viewBox="0 0 50 100"><polyline points="4,2 46,50 4,98" fill="none" stroke="#999" stroke-width="2"/></svg>
  <div class="speaker-photo abs"><div role="img" aria-label="Photo of a speaker presenting to an audience in front of a screen"></div></div>
  <div class="speaker-card abs">
    <div class="mic"><svg width="30" height="30" viewBox="0 0 30 30"><circle cx="19" cy="11" r="7" fill="#0b3f7a"/><line x1="14" y1="16" x2="4" y2="27" stroke="#0b3f7a" stroke-width="4" stroke-linecap="round"/></svg></div>
    <h4>Daniel Morrow</h4>
    <p>Lorem ipsum dolor sit amet, consectetuer adipiscing elit, sed diam nonummy nibh euismod tincidunt ut laoreet dolore magna aliquam erat volutpat. Ut enim ad minim veniam. Nam liber tempor cum soluta nobis eleifend option congue nihil imperdiet doming id quod mazim placerat facer possim assum. Nam liber tempor cum soluta nobis eleifend option congue nihil imperdiet doming id quod mazim placerat facer possim assum.</p>
    <span class="btn">Read More &#8250;</span>
  </div>
</section>

<section class="courses">
  <div class="abs" style="left:72px;top:3283px"><div class="eyebrow">Lorem ipsum dolor</div><h2>Upcoming Courses</h2><div class="rule"></div></div>
  <div class="view-more abs" style="left:1015px;top:3314px">View More &#8250;</div>

  <article class="course abs" style="left:72px;top:3413px"><div class="ph" role="img" aria-label="Photo of paintbrushes in a jar" style="background:linear-gradient(135deg,#3a2c22,#8a6a4a 50%,#d7c2a4)"></div><h4>Art</h4><p>Lorem ipsum dolor sit amet, consectetuer adipiscing elit, sed diam nonummy nibh euismod tincidunt.</p><svg class="circle-arrow" viewBox="0 0 24 24"><circle cx="12" cy="12" r="10" fill="none" stroke="var(--orange)" stroke-width="2.5"/><path d="M7 12h9M12 8l4 4-4 4" fill="none" stroke="var(--orange)" stroke-width="2.5"/></svg></article>
  <article class="course abs" style="left:342px;top:3413px"><div class="ph" role="img" aria-label="Photo of a photographer holding a camera" style="background:linear-gradient(135deg,#6f7d5a,#2c2f2a 50%,#a68a6a)"></div><h4>Photography</h4><p>Lorem ipsum dolor sit amet, consectetuer adipiscing elit, sed diam nonummy nibh euismod tincidunt.</p><svg class="circle-arrow" viewBox="0 0 24 24"><circle cx="12" cy="12" r="10" fill="none" stroke="var(--orange)" stroke-width="2.5"/><path d="M7 12h9M12 8l4 4-4 4" fill="none" stroke="var(--orange)" stroke-width="2.5"/></svg></article>
  <article class="course abs" style="left:613px;top:3413px"><div class="ph" role="img" aria-label="Photo of a runner on a trail at sunset" style="background:linear-gradient(160deg,#e2c08a,#b0845a 50%,#5a4634)"></div><h4>Health &amp; Fitness</h4><p>Lorem ipsum dolor sit amet, consectetuer adipiscing elit, sed diam nonummy nibh euismod tincidunt.</p><svg class="circle-arrow" viewBox="0 0 24 24"><circle cx="12" cy="12" r="10" fill="none" stroke="var(--orange)" stroke-width="2.5"/><path d="M7 12h9M12 8l4 4-4 4" fill="none" stroke="var(--orange)" stroke-width="2.5"/></svg></article>
  <article class="course abs" style="left:884px;top:3413px"><div class="ph" role="img" aria-label="Photo of financial charts on paper with a calculator" style="background:linear-gradient(135deg,#dfe6ee,#8fa3bd 50%,#2f3f58)"></div><h4>Financial</h4><p>Lorem ipsum dolor sit amet, consectetuer adipiscing elit, sed diam nonummy nibh euismod tincidunt.</p><svg class="circle-arrow" viewBox="0 0 24 24"><circle cx="12" cy="12" r="10" fill="none" stroke="var(--orange)" stroke-width="2.5"/><path d="M7 12h9M12 8l4 4-4 4" fill="none" stroke="var(--orange)" stroke-width="2.5"/></svg></article>
</section>

<footer>
  <div class="footer abs"></div>
  <div class="contact-col abs" style="left:208px">
    <div class="contact-head"><span class="ic"><svg width="28" height="28" viewBox="0 0 28 28"><path d="M6 3l5 1 2 6-3 2c1.5 3 3.5 5 6 6l2-3 6 2 1 5c-1 2-3 3-5 3C11 25 3 17 3 8c0-2 1-4 3-5z" fill="#fff"/></svg></span><h3>Get in Touch<br><span>With Us</span></h3></div>
    <p>Lorem ipsum dolor sit amet, consectetuer adipiscing elit, sed diam nonummy nibh euismod tincidunt.</p>
    <p class="small">Your Company LTD, Street Name, 000000, City Name</p>
    <p class="small">Phone: 1-555-010-0199 &nbsp;&nbsp;&nbsp; Email: hello@harborloft.example<br>View on Map</p>
  </div>
  <div class="contact-col abs" style="left:660px">
    <div class="contact-head"><span class="ic"><svg width="30" height="22" viewBox="0 0 30 22"><rect x="1" y="1" width="28" height="20" fill="#fff"/><polyline points="1,1 15,12 29,1" fill="none" stroke="#0b3f7a" stroke-width="2"/></svg></span><h3>Subscribe to<br><span>Our Newsletter</span></h3></div>
    <p>Lorem ipsum dolor sit amet, consectetuer adipiscing elit, sed diam nonummy nibh euismod tincidunt.</p>
    <div class="sub-form"><div class="field">Email Address</div><div class="send">Subscribe</div></div>
  </div>

  <div class="bottom-bar abs"></div>
  <div class="brand abs" style="top:4238px;left:86px"><span class="brand-square"></span><span class="brand-name">The Harbor Loft</span></div>
  <div class="socials abs"><span></span><span></span><span></span><span></span><span></span><span></span></div>
  <div class="copyright abs">Copyright © 2016 The Harbor Loft. All Rights Reserved<br>Privacy Policy &nbsp;&nbsp; Terms Of Use &nbsp;&nbsp; Sitemap</div>
</footer>

</body>
</html>
```